dkfarrowplace website

I need a new homepage design for my current website at www.DKFarrowPlace.example. I want someone to look at my current website and develop a more appealing homepage... right now the colors don't blend very well and it needs a facelift

Reason: This has been extended to September 10th

```html
<!DOCTYPE html>
<html lang="en">
<head>
<meta charset="utf-8">
<title>D K Farrow – Home</title>
<link rel="stylesheet" href="https://fonts.googleapis.com/css2?family=Ubuntu:wght@400;500;700&family=Open+Sans:wght@400;600;700&family=Arimo:wght@400;700&display=swap">
<style>
:root{
  --brand:#a0105a;
  --brand-dark:#7d0a45;
  --ink:#2b2b2b;
  --panel-dark:#2d2d2d;
  --footer:#3e3e3e;
  --hero-top:#d8d8d8;
  --hero-bottom:#f2f2f2;
  --box:#e9e9e9;
  --box-line:#d2d2d2;
  --white:#ffffff;
}
*{margin:0;padding:0;box-sizing:border-box}
html,body{width:868px;height:1200px;overflow:hidden;background:var(--white)}
body{position:relative;font-family:"Open Sans",sans-serif;color:var(--ink)}
.abs{position:absolute}

/* header */
.site-header{position:absolute;left:0;top:0;width:868px;height:68px;background:var(--brand)}
.brand{left:72px;top:8px;font-family:"Ubuntu",sans-serif;font-weight:500;font-size:19px;color:var(--white);letter-spacing:1px}
.main-nav{left:73px;top:40px;display:flex;gap:22px;font-size:12px;color:var(--white);font-weight:600;white-space:nowrap}
.call-us{left:655px;top:16px;font-size:12px;color:var(--white);white-space:nowrap}
.call-us b{font-weight:700}
.site-search{left:655px;top:38px;width:138px;height:19px;background:var(--white);border-radius:3px;font-size:9px;padding:4px 6px;color:#333}
.site-search svg{position:absolute;right:4px;top:3px}

/* hero */
.hero{left:0;top:68px;width:868px;height:554px;background:linear-gradient(160deg,var(--hero-top) 0%,var(--hero-bottom) 45%,#e2e2e2 100%);overflow:hidden}
.hero-swoosh{left:0;top:0}
.hero-photo{left:24px;top:12px;width:336px;height:480px;border-radius:160px 160px 40px 40px;background:linear-gradient(180deg,#e6c88d 0%,#e9c2a8 35%,#c51d6a 70%,#b9195f 100%)}
.label-after{left:73px;top:224px;font-weight:700;font-size:13px;color:#333}
.testimonial-title{left:402px;top:120px;font-family:"Ubuntu",sans-serif;font-weight:700;font-size:33px;color:var(--brand);white-space:nowrap}
.testimonial{left:402px;top:166px;width:368px;font-family:"Arimo",sans-serif;font-size:9px;line-height:14.5px;color:#333}
.testimonial-text{text-align:center}
.testimonial-author{font-weight:700;margin-left:3px}
.before-photo{left:405px;top:256px;width:106px;height:106px;border-radius:50%;border:4px solid var(--white);box-shadow:0 1px 4px rgba(0,0,0,.25);background:linear-gradient(180deg,#e6cf9c 0%,#e6c0a8 50%,#c01d67 100%)}
.label-before{left:518px;top:328px;font-weight:700;font-size:13px;color:#333}

/* free report */
.report{left:72px;top:493px;width:723px;height:192px;border-radius:5px;background:var(--panel-dark);overflow:hidden}
.report-head{position:absolute;left:0;top:0;width:100%;height:46px;background:var(--brand);color:var(--white);font-family:"Arimo",sans-serif;font-size:18px;padding:13px 0 0 64px;white-space:nowrap}
.report-head b{font-weight:700;margin-right:12px}
.report-lede{left:0;top:59px;width:100%;text-align:center;color:var(--white);font-size:13px;white-space:nowrap}
.report-lede b{font-size:16px}
.report-book{left:72px;top:92px;width:43px;height:58px;background:linear-gradient(160deg,#f4f4f4,#cfd6e6);border-left:4px solid #2f5bb0}
.field{background:var(--white);border-radius:3px;border:1px solid #bbb;font-size:8.5px;color:#444;padding:4px 8px}
.f-name{left:141px;top:98px;width:169px;height:21px}
.f-email{left:141px;top:126px;width:169px;height:21px}
.f-msg{left:327px;top:96px;width:169px;height:50px}
.subscribe{left:511px;top:112px;width:111px;height:32px;border-radius:6px;background:linear-gradient(180deg,#c01b6e,var(--brand-dark));color:var(--white);font-weight:700;font-size:12px;text-align:center;line-height:32px}
.report-privacy{left:0;top:160px;width:100%;text-align:center;color:var(--white);font-family:"Arimo",sans-serif;font-size:8px;white-space:nowrap}

/* ebooks */
.ebooks{left:71px;top:698px;width:726px;height:186px;background:var(--box);border:2px solid var(--box-line);border-radius:6px}
.ebook-divider{left:334px;top:6px;height:172px;border-left:1px dashed #bdbdbd}
.ebook{width:320px;height:180px}
.ebook h3{position:absolute;left:12px;top:8px;font-family:"Ubuntu",sans-serif;font-size:15px;font-weight:500;color:#333}
.ebook p{position:absolute;left:12px;top:29px;font-family:"Ubuntu",sans-serif;font-size:13px;color:#444;white-space:nowrap}
.ebook-cover{position:absolute;left:12px;top:55px;width:302px;height:86px;border-radius:6px;background:var(--brand)}
.ebook-cover span{position:absolute;left:5px;top:0;width:297px;height:81px;border-radius:6px;background:linear-gradient(90deg,#f2f7e6,#cfe9b4 70%,#a9d98a)}
.learn-more{position:absolute;left:20px;top:158px;font-size:9.5px;color:#333;letter-spacing:.3px;display:flex;align-items:center;gap:5px}

/* as seen in */
.seen{left:71px;top:906px;width:726px;height:152px;background:var(--box);border:2px solid var(--box-line);border-radius:6px;overflow:hidden}
.seen-head{position:absolute;left:0;top:0;width:100%;height:37px;background:var(--brand);color:var(--white);font-family:"Ubuntu",sans-serif;font-size:17px;font-weight:500;padding:8px 0 0 14px}
.seen-arrows{position:absolute;right:13px;top:10px;display:flex;gap:3px}
.seen-arrows div{width:19px;height:18px;background:#888;border-radius:2px;color:var(--white);font-size:11px;text-align:center;line-height:18px}
.outlet{position:absolute;top:69px;height:48px;background:var(--white);font-family:"Ubuntu",sans-serif;font-weight:700;font-size:18px;display:flex;align-items:center;justify-content:center;white-space:nowrap}

/* footer */
.site-footer{left:0;top:1079px;width:868px;height:121px;background:var(--footer);color:var(--white)}
.foot-title{font-family:"Ubuntu",sans-serif;font-size:15px;color:#e4e4e4}
.foot-left{left:71px;top:6px}
.foot-about{left:74px;top:31px;width:197px;font-size:8.8px;line-height:14.5px;text-align:justify;letter-spacing:.5px;color:#e8e8e8}
.foot-brand{left:71px;top:94px;font-family:"Ubuntu",sans-serif;font-weight:500;font-size:15px;letter-spacing:1px}
.foot-rule{top:8px;height:108px;border-left:1px dashed #777}
.foot-nav{left:296px;top:19px;width:304px;text-align:center;font-size:8px;font-family:"Arimo",sans-serif;white-space:nowrap}
.follow{left:296px;top:43px;width:304px;text-align:center;font-size:9px;font-family:"Arimo",sans-serif}
.socials{left:384px;top:57px;display:flex;gap:7px}
.socials span{width:28px;height:28px;border-radius:50%;background:#e7e7e7;border:2px solid #bbb}
.copyright{left:296px;top:104px;width:304px;text-align:center;font-size:8.5px;font-family:"Arimo",sans-serif;white-space:nowrap}
.foot-right{right:77px;top:9px;text-align:right}
.foot-address{right:77px;top:30px;text-align:right;font-size:9px;line-height:11.8px;letter-spacing:.4px;color:#ddd;white-space:nowrap}
.foot-phone{left:622px;top:86px;display:flex;align-items:center;gap:14px;font-family:"Ubuntu",sans-serif;font-weight:700;font-size:21px;color:#e4e4e4;white-space:nowrap}
</style>
</head>
<body>

<header class="site-header">
  <div class="abs brand">D K Farrow</div>
  <nav class="abs main-nav">
    <span>Home</span><span>About Us</span><span>Product Reviews</span><span>Blog</span><span>Forum</span><span>Media Room</span><span>Success Stories</span>
  </nav>
  <div class="abs call-us"><b>Call Us at:</b> 01632 960415</div>
  <div class="abs site-search">Site Search
    <svg width="13" height="13" viewBox="0 0 13 13"><circle cx="5.5" cy="5.5" r="4" fill="none" stroke="#333" stroke-width="1.5"/><line x1="8.5" y1="8.5" x2="12" y2="12" stroke="#333" stroke-width="2"/></svg>
  </div>
</header>

<section class="abs hero">
  <svg class="abs hero-swoosh" width="868" height="554" viewBox="0 0 868 554">
    <path d="M0 120 C120 210 200 380 230 554 L160 554 C130 400 80 260 0 180Z" fill="#c9c9c9" opacity=".6"/>
    <path d="M520 0 C640 60 760 140 868 140 L868 60 C770 60 660 30 600 0Z" fill="#ffffff" opacity=".6"/>
    <path d="M760 0 C800 80 840 120 868 130 L868 0Z" fill="#d0d0d0" opacity=".5"/>
  </svg>
  <div class="abs hero-photo" role="img" aria-label="Photo of a smiling woman in a pink top after her weight loss"></div>
  <div class="abs label-after">After</div>
  <h1 class="abs testimonial-title">I Have Lost 20 Pounds</h1>
  <div class="abs testimonial">
    <p class="testimonial-text">Lorem ipsum dolor sit amet, consectetur adipiscing elit. Quisque dapibus accumsan orci, pretium eleifend arcu adipiscing eget. Fusce accumsan facilisis tincidunt. Phasellus tempor enim purus, vitae venenatis est. Ut imperdiet hendrerit pulvinar. Cras at tellus a enim condimentum mollis ut et tellus. Mauris dolor magna, elementum eu dictum eu,</p>
    <p class="testimonial-author">- Lena Marsh Corvin</p>
  </div>
  <div class="abs before-photo" role="img" aria-label="Round portrait of the same woman before her weight loss"></div>
  <div class="abs label-before">Before</div>
</section>

<section class="abs report">
  <div class="report-head"><b>Free Report !</b> “ Five Reasons You Can Not Loose Your Weight ”</div>
  <p class="abs report-lede">Just enter your name and email below to get instant access to this 30 page report absolutely <b>FREE!</b></p>
  <div class="abs report-book" role="img" aria-label="Cover of the free report booklet"></div>
  <div class="abs field f-name">Your Name</div>
  <div class="abs field f-email">Email</div>
  <div class="abs field f-msg">Your Message</div>
  <div class="abs subscribe">Subscribe</div>
  <p class="abs report-privacy">E-mail Privacy: Sign up with complete confidence! We will never sell, rent, lease, or share your information with anyone.</p>
</section>

<section class="abs ebooks">
  <div class="abs ebook" style="left:0;top:0">
    <h3>Our E-books</h3>
    <p>Nutritionist and Weight- Loss Expert</p>
    <div class="ebook-cover"><span role="img" aria-label="Banner for a green smoothie cleanse e-book"></span></div>
    <div class="learn-more">Learn more <svg width="9" height="9" viewBox="0 0 9 9"><circle cx="4.5" cy="4.5" r="4.5" fill="var(--brand)"/><path d="M3.5 2.5 L5.5 4.5 L3.5 6.5" stroke="#fff" stroke-width="1.3" fill="none"/></svg></div>
  </div>
  <div class="abs ebook-divider"></div>
  <div class="abs ebook" style="left:360px;top:0">
    <h3>Our E-books</h3>
    <p>Nutritionist and Weight- Loss Expert</p>
    <div class="ebook-cover"><span role="img" aria-label="Banner for a green smoothie cleanse e-book"></span></div>
    <div class="learn-more">Learn more <svg width="9" height="9" viewBox="0 0 9 9"><circle cx="4.5" cy="4.5" r="4.5" fill="var(--brand)"/><path d="M3.5 2.5 L5.5 4.5 L3.5 6.5" stroke="#fff" stroke-width="1.3" fill="none"/></svg></div>
  </div>
</section>

<section class="abs seen">
  <div class="seen-head">As Seen In
    <div class="seen-arrows"><div>&lt;</div><div>&gt;</div></div>
  </div>
  <div class="outlet" style="left:8px;width:138px;color:#c8512b">Hearth Weekly</div>
  <div class="outlet" style="left:170px;width:90px;color:#1a2f7a">NOVA</div>
  <div class="outlet" style="left:285px;width:154px;color:#b31d3b">Lumen.example</div>
  <div class="outlet" style="left:464px;width:138px;color:#1f5bb0">OrbitWave</div>
  <div class="outlet" style="left:631px;width:82px;color:#2e7d1f">KV9</div>
</section>

<footer class="abs site-footer">
  <div class="abs foot-title foot-left">Contact Info</div>
  <p class="abs foot-about">Lorem ipsum dolor sit amet, consectetuer adipiscing elit. Donec libero. Suspendisse bibendum. Cras id urna. Morbi tincidunt,</p>
  <div class="abs foot-brand">D K Farrow</div>
  <div class="abs foot-rule" style="left:296px"></div>
  <div class="abs foot-rule" style="left:600px"></div>
  <div class="abs foot-nav">Home &nbsp;~&nbsp; About Us &nbsp;~&nbsp; Service &nbsp;~&nbsp; Environment &nbsp;~&nbsp; Contact Us</div>
  <div class="abs follow">Follow Us On:</div>
  <div class="abs socials"><span></span><span></span><span></span><span></span></div>
  <div class="abs copyright">Copyright (c) dkfarrowplace, All Right Reserved &nbsp;2014-15, Privacy Policy</div>
  <div class="abs foot-title foot-right">Contact Info</div>
  <div class="abs foot-address">Merry healthy: 42 118 507 223<br>9 Harrow Lane<br>Elmbrook<br>Vic. 3999<br><b>Email:</b> info@dkfarrowplace.example</div>
  <div class="abs foot-phone">
    <svg width="26" height="26" viewBox="0 0 26 26"><circle cx="13" cy="13" r="11.5" fill="none" stroke="#ddd" stroke-width="1.5"/><path d="M9 7 L11 7 L12 10 L10.5 11.5 C11.3 13.5 12.5 14.7 14.5 15.5 L16 14 L19 15 L19 17 C19 18 18 19 17 19 C11.5 18.5 7.5 14.5 7 9 C7 8 8 7 9 7Z" fill="#ddd"/></svg>
    555-0142-907
  </div>
</footer>

</body>
</html>
```